Dietetic office: Bright Plate

I want to give my business card a modern and warm look (which attracts the eye and has a reassuring side), which links dietetics to a moment of well-being. The front and back sides must be used (not just to put the logo on the front side)

The map should be eye-catching and easy to read. I don't necessarily want to have a plain background, which I find visually weighs down the maps.
I really like the square format of a business card with rounded edges which is different from what we are used to finding (and why not take this square diagonally?), however I am not closed to another format as long as I like the style.

Who am I? Mireille, 32 years old, Dietician and passionate about food since always. I am specialized in slimming and an expert in micro nutrition, which means that I take into account not only the nutritional balance while maintaining pleasure (if foods are present in the business card, I do not want some cliché things where there would just be fruits and vegetables, but really something more global), but also the psycho-emotional dimension that I will treat with food supplements based on plants, fruits or vegetables.

-----------------------------------------------------------------------------------

 Mention to appear on the card IN FRENCH (please be careful in case of translation that the use of words is correct):

Mireille DORAN
Dietician Nutritionist
Expert in Slimming and Micro-Nutrition

Slogan: I help you lose weight sustainably with pleasure and by reconciling your events

Catchphrases: Want to lose weight? Do you like going out? Do you have a lot of events? And is pleasure on your plate important to you?

Make an appointment on Rendiplan or on 06 41 58 30 92
mireille.brightplate@exemplo-mail.fr
Address: Health Center, Rue des Glycines, 13127 Vitrolles
www.brightplate-exemple.fr
Friendwall + Picturo Logo

- The company logo has been uploaded for your viewing. Other file formats can be made available if required.
- I would like a place for a photo of me to be possible.

Good morning,
I want to have a business card that is both lively and warm. Which will easily catch the eye while being easy to read and make people understand that I am in the field of well-being.
I like the square side in business cards (and why not use them diagonally?), or a more classic but original one.
Both the front and back sides must be used (I don't want to have the logo on just one side)
I don't want to have a plain background, but rather something more muted (I really like the suggestion from "Reed Cloud Graphic Designer" for this)
the use of logo for telephone, mail, address, rendiplan, friendwall, pictu etc is possible in order to facilitate reading

Please follow the various elements of the brief regarding the text and use the French text as it is.

I like business cards preferably square (with the possibility of using them diagonally).
The map should be eye-catching and easy to read.
It must bring pep while having softness which brings back to the well-being side
The card must be used on the front and back for the different elements (I do not want to have only the logo on the front side)
The text must correspond to the brief (be careful with the translation which can sometimes be bad)
I don't want to have a plain blue or orange background. I really like the idea of the background from "Reed Cloud Graphic Designer"

You can if you wish use symbols for contacts, telephone, rendiplan, address, fw, pictu....

Target Market(s)

mainly women between 25 and 65 years old + men around 40 years old

Contact Information for Business Card

Font styles to use
Sans Serif
Script

Colors
0054AA
0677BA
7BADD7
CADEEF
E8F1F8
0094D4
00A9DD
6FCCEA
C7EBF8
E9F6FB
00AB8E
00BBA5
67D7C9
C6EFE9
E9F9F6
FFC000
F8CF3A
FAE287
FDF2CF
FEFAEE
F0912C
F2A743
F7CA91
FBE8D2
FDF5EE

Requirements
Must have
• some pep! while being refined
Nice to have
• I really like the square format of a business card with rounded edges which is different from what we are used to finding, however I am not closed to another format as long as I like the style.
Should not have
• if foods are represented, only show fruits and vegetables (too cliché)

```html
<!DOCTYPE html>
<html lang="en">
<head>
<meta charset="utf-8">
<title>Bright Plate – Business Card</title>
<link href="https://fonts.googleapis.com/css2?family=Philosopher:wght@400;700&family=Poppins:wght@300;400;500;600;700&family=Roboto:wght@400&family=Roboto+Condensed:wght@400&display=swap" rel="stylesheet">
<style>
  :root {
    --page-bg: #dedede;
    --brand-blue: #0a7ad6;
    --name-blue: #0b6fcf;
    --brand-orange: #f7931e;
    --soft-orange: #fbe8d2;
    --aqua: #2bd3df;
    --white: #ffffff;
    --ink: #222222;
  }
  * { margin: 0; padding: 0; box-sizing: border-box; }
  html, body { width: 1200px; height: 866px; overflow: hidden; background: var(--page-bg); }
  .card {
    position: absolute; width: 429px; height: 429px; border-radius: 22px;
    overflow: hidden; background: var(--white);
  }
  .card--front { left: 151px; top: 207px; }
  .card--back { left: 632px; top: 201px; background: var(--brand-blue); }

  /* front */
  .front__illustration {
    position: absolute; left: 0; top: 0; width: 235px; height: 193px;
    background: linear-gradient(120deg, var(--brand-orange) 0%, #f9b968 45%, var(--white) 100%);
    opacity: .85;
  }
  .front__social {
    position: absolute; right: 16px; top: 32px; display: flex; gap: 8px;
    font-family: "Poppins", sans-serif; font-size: 11px; font-weight: 500; color: var(--name-blue);
  }
  .front__name {
    position: absolute; right: 22px; top: 74px;
    font-family: "Philosopher", sans-serif; font-size: 33px; font-weight: 400;
    color: var(--name-blue); letter-spacing: .3px; white-space: nowrap;
  }
  .front__title {
    position: absolute; right: 25px; top: 110px;
    font-family: "Roboto", sans-serif; font-size: 15.5px; color: var(--brand-orange);
  }
  .front__expertise {
    position: absolute; right: 25px; top: 133px;
    font-family: "Roboto Condensed", sans-serif; font-size: 15.5px; color: var(--ink);
  }
  .front__slogan {
    position: absolute; left: 0; top: 193px; width: 100%; height: 71px;
    background: var(--brand-blue); padding: 13px 22px 0 22px;
    font-family: "Poppins", sans-serif; font-size: 18.5px; line-height: 23px;
    color: var(--aqua); text-align: center;
  }
  .front__slogan strong { color: var(--white); font-weight: 600; }
  .front__contact {
    position: absolute; left: 0; top: 268px; width: 100%; height: 161px;
    background: var(--brand-orange); padding-top: 32px; text-align: center;
    font-family: "Roboto", sans-serif; font-size: 17px; line-height: 26px; color: var(--white);
  }

  /* back */
  .back__logo {
    position: absolute; left: 0; top: 78px; width: 100%; text-align: center;
    font-family: "Philosopher", sans-serif; font-size: 54px; font-weight: 400; color: var(--white);
  }
  .back__questions {
    position: absolute; left: 0; top: 192px; width: 100%; text-align: center;
    font-family: "Poppins", sans-serif; font-size: 23px; line-height: 28.5px;
  }
  .back__questions .q-light { color: var(--white); font-weight: 300; }
  .back__questions .q-accent { color: var(--aqua); font-weight: 500; }
  .back__cta {
    position: absolute; left: 0; top: 350px; width: 100%; height: 79px;
    background: var(--brand-orange); padding-top: 13px; text-align: center;
    font-family: "Poppins", sans-serif; font-size: 21px; line-height: 27px;
    color: var(--white); text-transform: uppercase;
  }
  .back__cta b { font-weight: 700; }
</style>
</head>
<body>
  <section class="card card--front">
    <div class="front__illustration" role="img" aria-label="Orange fork and spoon resting on a plate rim illustration"></div>
    <div class="front__social"><span>Picturo</span><span>Friendwall</span></div>
    <h1 class="front__name">Mireille DORAN</h1>
    <p class="front__title">Dietician Nutritionist</p>
    <p class="front__expertise">Expert in Slimming &amp; Micro-Nutrition</p>
    <p class="front__slogan"><strong>I help you lose weight sustainably</strong> with pleasure &amp; by reconciling your events</p>
    <address class="front__contact" style="font-style:normal">
      Health Center<br>
      Rue des Glycines, 13127 Vitrolles<br>
      mireille.brightplate@exemplo-mail.fr<br>
      www.brightplate-exemple.fr
    </address>
  </section>

  <section class="card card--back">
    <div class="back__logo">Bright Plate</div>
    <p class="back__questions">
      <span class="q-light">Want to lose weight?</span><br>
      <span class="q-accent">Do you like going out?</span><br>
      <span class="q-light">Do you have a lot of events?</span><br>
      <span class="q-accent">And the pleasure on your<br>plate is important to you?</span>
    </p>
    <p class="back__cta">Make an appointment <b>on<br>Rendiplan or on 06 41 58 30 92</b></p>
  </section>
</body>
</html>
```